Move the hackers to Wordpress

Yep, we want to move https://www.brasslantern.com/ to Wordpress. It'll make it easier to update and add content. I'd like mostly the same look, but I'm not stuck with it.
Updates

DO NOT RESPOND OUTSIDE OF PIXEL BAZAAR OR CONTACT US DIRECTLY.

Industry/Entity Type

Computer Security

Coding

Coded - Design and coding required

Font styles to use
Sans Serif

Colors
ec1f27

Requirements
Must have
• What I do want is:
• 1. Similar look to the existing site
• 2. Needs to work on one of the Wordpress hosting sites. I do NOT want to run my own Wordpress server.
• 3. Keep the animation in the top panel.
• 4. Mobile support
• The rest can be changed as needed.
Nice to have
• I like the transitions when the "services" panel shows up. Not stuck on it, but it is a nice touch.

```html
<!DOCTYPE html>
<html lang="en">
<head>
<meta charset="utf-8">
<title>Brass Lantern Information Security</title>
<link rel="stylesheet" href="https://fonts.googleapis.com/css2?family=Nunito:wght@400;600;700&family=Open+Sans:wght@400;600;700&display=swap">
<style>
:root{
  --brand-red:#ec1f27;
  --band-red:#b8231c;
  --band-red-dark:#8f1812;
  --ink:#222;
  --body-text:#4a4a4a;
  --white:#fff;
  --night:#0b0b0b;
  --star:#f4b400;
}
*{margin:0;padding:0;box-sizing:border-box}
html,body{width:1200px;height:2799px;overflow:hidden}
body{position:relative;background:var(--white);font-family:"Open Sans",Arial,sans-serif;color:var(--ink)}
.abs{position:absolute}
h1,h2,h3,h4{font-family:"Nunito","Open Sans",sans-serif;font-weight:600}

/* hero */
.hero{left:0;top:0;width:1200px;height:612px;clip-path:polygon(0 0,100% 0,100% 522px,0 612px);
  background:radial-gradient(ellipse at 50% 40%,#2c2c2c 0%,#141414 55%,#050505 100%)}
.brand{left:103px;top:38px;display:flex;align-items:center;gap:12px}
.brand-mark{width:56px;height:72px;background:var(--brand-red)}
.brand-name{color:var(--white);font-family:"Open Sans",sans-serif;font-weight:400;font-size:31px;letter-spacing:4px;line-height:1}
.brand-sub{color:var(--white);font-size:11px;letter-spacing:4.5px;margin-top:6px;font-weight:400}
.main-nav{right:102px;top:60px;display:flex;gap:21px;font-size:14px;color:var(--white)}
.hero-title{left:0;width:1200px;top:222px;text-align:center;color:var(--white);font-size:54px;line-height:60px;font-weight:600}
.btn{display:flex;align-items:center;justify-content:center;background:var(--brand-red);color:var(--white);font-family:"Open Sans",sans-serif;font-weight:600;font-size:19px;text-transform:uppercase}
.hero-btn{left:521px;top:375px;width:156px;height:47px}

/* about */
.section-title{font-size:40px;font-weight:600;color:var(--ink);letter-spacing:.5px}
.section-title span{color:var(--brand-red)}
.about-title{left:101px;top:713px}
.about-lead{left:101px;top:778px;width:460px;font-size:13px;font-weight:700;color:var(--ink)}
.about-text{left:101px;top:806px;width:452px;font-size:12.6px;line-height:26px;color:var(--body-text)}
.about-btn{left:101px;top:985px;width:158px;height:45px}
.video-back{left:634px;top:709px;width:484px;height:301px;background:var(--brand-red)}
.video-frame{left:603px;top:728px;width:498px;height:302px;background:radial-gradient(ellipse at 55% 45%,#5a6670 0%,#2b3036 45%,#0e1012 100%);box-shadow:0 8px 18px rgba(0,0,0,.35)}
.play{left:818px;top:846px;width:66px;height:66px}

/* services */
.services{left:0;top:1148px;width:1200px;height:606px;clip-path:polygon(0 0,100% 47px,100% 100%,0 559px);
  background:radial-gradient(ellipse at 50% 45%,#c9302a 0%,var(--band-red) 50%,var(--band-red-dark) 100%)}
.services-title{left:0;top:1252px;width:1200px;text-align:center;color:var(--white);font-size:40px}
.services-title strong{font-weight:700}
.service{width:310px;color:var(--white)}
.service svg{position:absolute;left:0;top:0;width:42px;height:42px}
.service h3{margin-left:54px;font-family:"Open Sans",sans-serif;font-size:13.5px;font-weight:600;line-height:24px;text-transform:uppercase}
.service p{margin-left:54px;margin-top:8px;width:236px;font-size:11.5px;line-height:21px;text-align:justify}

/* clients */
.clients-title{left:0;top:1846px;width:1200px;text-align:center}
.client{width:314px;height:187px;background:var(--white);border-radius:10px;box-shadow:0 6px 16px rgba(0,0,0,.14)}
.avatar{position:absolute;left:12px;top:30px;width:64px;height:64px;border-radius:50%;background:radial-gradient(circle at 50% 40%,#d9c1ab 0%,#b9b9b9 60%,#e9e9e9 100%)}
.stars{position:absolute;left:90px;top:26px;color:var(--star);font-size:17px;letter-spacing:1px}
.quote{position:absolute;left:90px;top:52px;width:210px;font-size:12px;line-height:26px;color:var(--ink)}
.client-name{position:absolute;left:90px;top:142px;font-size:13.5px;font-weight:700;color:var(--brand-red)}

/* footer */
.footer{left:0;top:2230px;width:1200px;height:569px;clip-path:polygon(0 84px,100% 0,100% 100%,0 100%);
  background:linear-gradient(180deg,#151515 0%,var(--night) 60%,#000 100%)}
.foot-col{color:var(--white)}
.foot-col h4{font-family:"Nunito",sans-serif;font-size:21px;font-weight:600;margin-bottom:18px}
.foot-links{list-style:none;font-size:12.5px;line-height:31px}
.foot-links li::before{content:"»";margin-right:8px}
.contact-list{font-size:12px;line-height:27px}
.contact-list b{font-weight:700;display:flex;align-items:center;gap:10px}
.contact-list b svg{width:12px;height:12px}
.contact-list span{display:block;padding-left:22px}
.newsletter{left:862px;top:2448px;width:239px;height:47px;border:1.5px solid var(--white);color:var(--white);font-size:12px;display:flex;align-items:center;justify-content:space-between;padding:0 16px}
.social{top:2525px;width:36px;height:36px;border:1.5px solid var(--white);border-radius:50%}
.foot-rule{left:101px;top:2743px;width:1004px;height:1px;background:#555}
.copyright{left:0;top:2762px;width:1200px;text-align:center;color:var(--white);font-size:12px}
</style>
</head>
<body>

<header class="abs hero" role="img" aria-label="Dark background of glowing hexagon grid with padlock symbols and binary code"></header>
<div class="abs brand">
  <div class="brand-mark"></div>
  <div>
    <div class="brand-name">BRASS LANTERN</div>
    <div class="brand-sub">INFORMATION SECURITY</div>
  </div>
</div>
<nav class="abs main-nav"><span>Home</span><span>About Us</span><span>Services</span><span>Blog</span><span>Press</span><span>Contact Us</span></nav>
<h1 class="abs hero-title">OFFENSIVE SERVICES FROM<br>OFFENSIVE MINDS</h1>
<div class="abs btn hero-btn">Read More</div>

<h2 class="abs section-title about-title"><span>ABOUT</span> US</h2>
<p class="abs about-lead">We are an information security company focusing on real world threats.</p>
<p class="abs about-text">Brass Lantern is an information security consulting company that concentrates on the latest threats to organizations today. We perform in-depth analysis, deter mine organization/business risk, and find the vulnerabilities before the bad guys do. Our team includes internationally renowned experts who have been featured in international news outlets and conferences, including The Daily Ledger, The Capital Post, a Harbor News Network Documentary.</p>
<div class="abs btn about-btn">Read More</div>
<div class="abs video-back"></div>
<div class="abs video-frame" role="img" aria-label="Video still: close-up of an eye behind dark-rimmed glasses reflecting a screen"></div>
<svg class="abs play" viewBox="0 0 66 66"><circle cx="33" cy="33" r="31" fill="#ec1f27" stroke="#fff" stroke-width="3"/><path d="M26 21 L46 33 L26 45Z" fill="#fff"/></svg>

<section class="abs services" role="img" aria-label="Red band with faint hooded figure and world map in the background"></section>
<h2 class="abs services-title">OUR <strong>SERVICES</strong></h2>

<div class="abs service" style="left:99px;top:1346px">
  <svg viewBox="0 0 42 42" fill="#fff"><circle cx="21" cy="5" r="4"/><circle cx="32" cy="10" r="3.5"/><circle cx="37" cy="21" r="3"/><circle cx="32" cy="32" r="2.6"/><circle cx="21" cy="37" r="2.3"/><circle cx="10" cy="32" r="2"/><circle cx="5" cy="21" r="1.8"/><circle cx="10" cy="10" r="1.5"/></svg>
  <h3>Internal Pivot Assessment<br>&amp; Post Exploitation</h3>
  <p>We start as a low privilege user and attempt to move through the network in an attempt to access the data....</p>
</div>
<div class="abs service" style="left:452px;top:1346px">
  <svg viewBox="0 0 42 42" fill="#fff"><circle cx="21" cy="10" r="6"/><circle cx="9" cy="14" r="4.5"/><circle cx="33" cy="14" r="4.5"/><path d="M11 34c0-8 4-14 10-14s10 6 10 14z"/><path d="M1 32c0-7 3-11 8-11 2 0 3 1 4 2-2 3-3 6-3 9z"/><path d="M41 32c0-7-3-11-8-11-2 0-3 1-4 2 2 3 3 6 3 9z"/></svg>
  <h3>Red Team Adversary<br>Simulation</h3>
  <p>A goal-based assessment where we attack just like a real world adversary. This includes external attacks....</p>
</div>
<div class="abs service" style="left:802px;top:1346px">
  <svg viewBox="0 0 42 42" fill="none" stroke="#fff"><circle cx="15" cy="24" r="8" stroke-width="6" stroke-dasharray="4 2.3"/><circle cx="15" cy="24" r="3" stroke-width="3"/><circle cx="32" cy="10" r="5" stroke-width="4" stroke-dasharray="3 1.8"/><circle cx="32" cy="33" r="4" stroke-width="3.5" stroke-dasharray="2.5 1.6"/></svg>
  <h3>Penetration Testing &amp;<br>Vulnerability Assessments</h3>
  <p>This includes vulnerability scans of the in-scope systems where we manually verify issues...</p>
</div>
<div class="abs service" style="left:99px;top:1518px">
  <svg viewBox="0 0 42 42" fill="none" stroke="#fff" stroke-width="3.5"><path d="M2 12h8c8 0 12 18 20 18h6"/><path d="M2 30h8c8 0 12-18 20-18h6"/><path d="M33 7l6 5-6 5M33 25l6 5-6 5" stroke-width="3"/></svg>
  <h3>Advanced Product, RF Testing<br>&amp; Hardware</h3>
  <p>We start as a low privilege user and attempt to move through the network in an attempt to access the data....</p>
</div>
<div class="abs service" style="left:452px;top:1518px">
  <svg viewBox="0 0 42 42" fill="#fff"><path d="M3 6h36v24H3zM7 10v16h28V10z" fill-rule="evenodd"/><rect x="17" y="30" width="8" height="5"/><rect x="12" y="35" width="18" height="3"/></svg>
  <h3>Web Application Penetration<br>Testing</h3>
  <p>A goal-based assessment where we attack just like a real world adversary. This includes external attacks....</p>
</div>
<div class="abs service" style="left:802px;top:1518px">
  <svg viewBox="0 0 42 42" fill="#fff"><path d="M13 2h16a3 3 0 0 1 3 3v32a3 3 0 0 1-3 3H13a3 3 0 0 1-3-3V5a3 3 0 0 1 3-3zM13 7v24h16V7z" fill-rule="evenodd"/><circle cx="21" cy="35" r="2" fill="#b8231c"/></svg>
  <h3>Mobile Application<br>Assessment</h3>
  <p>This includes vulnerability scans of the in-scope systems where we manually verify issues...</p>
</div>

<h2 class="abs section-title clients-title"><span>HAPPY</span> CLIENTS</h2>
<div class="abs client" style="left:101px;top:1931px">
  <div class="avatar" role="img" aria-label="Client portrait photo"></div>
  <div class="stars">★★★★☆</div>
  <p class="quote">Lorem ipsum dolor sit amet conseca tet adpis elit sed do eiusmo tempor incid idunt lnim ad minim.</p>
  <div class="client-name">Marten Elsworth</div>
</div>
<div class="abs client" style="left:444px;top:1931px">
  <div class="avatar" role="img" aria-label="Client portrait photo"></div>
  <div class="stars">★★★★☆</div>
  <p class="quote">Lorem ipsum dolor sit amet conseca tet adpis elit sed do eiusmo tempor incid idunt lnim ad minim.</p>
  <div class="client-name">Tobias Verdonk</div>
</div>
<div class="abs client" style="left:786px;top:1931px">
  <div class="avatar" role="img" aria-label="Client portrait photo"></div>
  <div class="stars">★★★★☆</div>
  <p class="quote">Lorem ipsum dolor sit amet conseca tet adpis elit sed do eiusmo tempor incid idunt lnim ad minim.</p>
  <div class="client-name">Idris Van Castel</div>
</div>

<footer class="abs footer" role="img" aria-label="Black background with faint falling binary code"></footer>
<div class="abs foot-col" style="left:99px;top:2395px">
  <h4>Quick Links</h4>
  <ul class="foot-links"><li>Home</li><li>About Us</li><li>Services</li><li>Blog</li><li>Press</li><li>Contact Us</li></ul>
</div>
<div class="abs foot-col" style="left:336px;top:2395px">
  <h4>Support</h4>
  <ul class="foot-links"><li>Terms of Use</li><li>Private Policy</li></ul>
</div>
<div class="abs foot-col" style="left:578px;top:2399px">
  <h4>Contact Info</h4>
  <div class="contact-list">
    <b><svg viewBox="0 0 12 12" fill="#fff"><path d="M6 0a4 4 0 0 1 4 4c0 3-4 8-4 8S2 7 2 4a4 4 0 0 1 4-4zm0 2.5a1.5 1.5 0 1 0 0 3 1.5 1.5 0 0 0 0-3z" fill-rule="evenodd"/></svg>Our Address</b>
    <span>14 Copperfield Lane PO Box</span>
    <span>3318 Eastbrook, 2290</span>
    <b><svg viewBox="0 0 12 12" fill="#fff"><path d="M2 0l2.5 2.8-1.3 1.6c.8 1.8 2.4 3.4 4.4 4.4l1.6-1.3L12 10l-2 2C4.5 11.5.5 7.5 0 2z"/></svg>Phone Number</b>
    <span>555 014 2271</span>
    <b><svg viewBox="0 0 12 12" fill="#fff"><path d="M0 2h12v8H0zM1 3l5 4 5-4" stroke="#000" stroke-width=".8"/></svg>Email Address</b>
    <span>contact@brasslantern.com</span>
  </div>
</div>
<div class="abs foot-col" style="left:860px;top:2399px"><h4>Newsletter</h4></div>
<div class="abs newsletter"><span>Enter The Email</span><span>→</span></div>
<div class="abs social" style="left:861px" aria-label="Social profile link"></div>
<div class="abs social" style="left:908px" aria-label="Social profile link"></div>
<div class="abs social" style="left:956px" aria-label="Social profile link"></div>
<div class="abs foot-rule"></div>
<p class="abs copyright">Copyrights © 2018.All rights reserved. Terms | Privacy</p>

</body>
</html>
```